Werbebrief
Zielgruppe
Unsere Zielgruppe sind Geschäftsführer junger Unternehmen.
Hallo,
Wir benötigen einen "Werbebrief". Es ist jedoch weniger ein Brief, als viel mehr eine etwas größerer "Werbekarte" (diese soll 105 x 210mm groß sein).
Auf der Vorderseite soll folgender Text stehen:
Für Unternehmen, die gerne expandieren möchten
Auf der Rückseite soll folgender Link stehen:
www.tolvek-werk.de/Expandieren
Darunter soll folgendes stehen:
Ihr persönlicher Code: ABC123
Wichtig ist, dass wir den Code individuell ändern können, da jeder einen anderen Code bekommt.
Unser Logo und Corporate Farbe habe ich hochgeladen. Das Design sollte auf jeden Fall zu unserer Webseite passen (www.tolvek-werk.de)
Wir freuen uns auf Ihre Vorschläge.

```html
<!DOCTYPE html>
<html lang="de">
<head>
<meta charset="utf-8">
<title>Werbekarte – Tolvek Werk</title>
<link rel="stylesheet" href="https://fonts.googleapis.com/css2?family=Ubuntu:wght@300;400&display=swap">
<style>
  :root {
    --page-bg: #e8e8e6;
    --brand-blue: #1f4e97;
    --brand-blue-light: #2b5ca8;
    --divider: rgba(255,255,255,0.75);
    --paper: #ffffff;
    --paper-shade: #e6e6e6;
    --text-light: #ffffff;
  }
  * { box-sizing: border-box; margin: 0; padding: 0; }
  html, body {
    width: 1200px; height: 1200px; overflow: hidden;
    background: var(--page-bg);
    font-family: "Ubuntu", sans-serif;
  }
  .canvas {
    position: relative; width: 1200px; height: 1200px;
  }
  .sheet {
    position: absolute; top: 200px;
    width: 470px; height: 800px;
    display: flex; flex-direction: column;
    box-shadow: 0 6px 18px rgba(0,0,0,0.18);
  }
  .sheet--front { left: 95px; }
  .sheet--back { left: 635px; }
  .card-face {
    position: relative; height: 280px;
    background: linear-gradient(160deg, var(--brand-blue-light), var(--brand-blue) 70%);
    color: var(--text-light);
  }
  .card-face + .card-face { border-top: 1.5px solid var(--divider); }
  .sheet-blank {
    flex: 1;
    background: linear-gradient(180deg, var(--paper-shade), var(--paper) 60%);
  }
  .brand {
    position: absolute; top: 20px; right: 22px;
    display: flex; align-items: center; gap: 10px;
    font-weight: 400; font-size: 22px; letter-spacing: 0.2px;
  }
  .brand-mark {
    width: 14px; height: 14px; background: var(--text-light);
  }
  .brand-name { padding-left: 10px; border-left: 2px solid var(--text-light); line-height: 1; }
  .tagline {
    position: absolute; top: 92px; left: 74px;
    font-weight: 300; font-size: 21px; line-height: 1.5;
  }
  .tagline span { display: block; }
  .tagline span:last-child { padding-left: 103px; }
  .offer {
    position: absolute; top: 92px; left: 40px; right: 40px;
    font-weight: 300; font-size: 21px; line-height: 1.45; text-align: right;
  }
  .offer-url { display: block; padding-right: 90px; }
  .offer-code { display: flex; justify-content: flex-end; align-items: center; gap: 6px; padding-right: 0; }
  .code-field {
    display: inline-block; width: 110px; height: 26px;
    background: var(--paper); color: var(--brand-blue);
    font-size: 16px; line-height: 26px; text-align: center;
  }
</style>
</head>
<body>
<main class="canvas">
  <section class="sheet sheet--front" aria-label="Vorderseite">
    <div class="card-face">
      <div class="brand"><span class="brand-mark"></span><span class="brand-name">Tolvek Werk</span></div>
      <p class="tagline"><span>Für Unternehmen, die gerne</span><span>expandieren möchten</span></p>
    </div>
    <div class="card-face">
      <div class="brand"><span class="brand-mark"></span><span class="brand-name">Tolvek Werk</span></div>
      <p class="tagline"><span>Für Unternehmen, die gerne</span><span>expandieren möchten</span></p>
    </div>
    <div class="sheet-blank"></div>
  </section>

  <section class="sheet sheet--back" aria-label="Rückseite">
    <div class="card-face">
      <div class="brand"><span class="brand-mark"></span><span class="brand-name">Tolvek Werk</span></div>
      <p class="offer">
        <span class="offer-url">www.tolvek-werk.de/Expandieren</span>
        <span class="offer-code">Ihr persönlicher Code:<span class="code-field"></span></span>
      </p>
    </div>
    <div class="card-face">
      <div class="brand"><span class="brand-mark"></span><span class="brand-name">Tolvek Werk</span></div>
      <p class="offer">
        <span class="offer-url">www.tolvek-werk.de/Expandieren</span>
        <span class="offer-code">Ihr persönlicher Code:<span class="code-field"></span></span>
      </p>
    </div>
    <div class="sheet-blank"></div>
  </section>
</main>
</body>
</html>
```